Business cards for Norwegian software consultancy business

We are in need of business cards for our Norwegian consultancy company.
“Talvik Brensor AS” specializes in software development, architecture and agile methodology, providing mostly on-site services at customers.
The cards should reflect a certain level of business professionalism with an elegant touch, while paying tribute to our modern and technological heritage. Our logo should be featured, as well as room for basic information about the cardholder and legal information of the company (company name, address and VAT number).
We would like our cards to reflect that we are a modern consulting company. It should present a professional image that people will remember. The texture and color pallette should reflect our professionalism and reliability, so we prefer a light color pallette with colors such as gray, white, blue and black. The number of colors used should however not be overwhelming, with the text being distinct and readable.
We are open to untraditional layouts and playful designs as long as they communicate the intent stated above.
You could also take a look at our website http://www.brensor.no for input on our visual profile.
Our logo is attached in the form of vectors and rasterized PNG. Please comment if you would like the black-white and/or inverted versions as well.
Architecture
Company information:
Talvik Brensor AS
Lindeholtveien 7, 3142 Vestskogen
461 82 915
info@brensor.no
www.brensor.no
Employee information:
Full name
Title
Email
Phone

```html
<!DOCTYPE html>
<html lang="en">
<head>
<meta charset="utf-8">
<title>Talvik Brensor AS – Business Cards</title>
<link href="https://fonts.googleapis.com/css2?family=Open+Sans:wght@400;700&display=swap" rel="stylesheet">
<style>
  :root {
    --backdrop: #e6e4e1;
    --brand-blue: #519fd4;
    --ink: #111111;
    --paper: #ffffff;
    --text: #1a1a1a;
  }
  html, body {
    margin: 0;
    padding: 0;
    width: 1200px;
    height: 749px;
    overflow: hidden;
    background: var(--backdrop);
    font-family: "Open Sans", Arial, sans-serif;
  }
  .stage {
    position: relative;
    width: 1200px;
    height: 749px;
  }
  .card {
    position: absolute;
    top: 200px;
    width: 545px;
    height: 310px;
    box-shadow: 0 14px 28px rgba(0, 0, 0, 0.18);
    overflow: hidden;
  }
  .card--front {
    left: 40px;
    background: var(--brand-blue);
  }
  .card--back {
    left: 621px;
    background: var(--paper);
  }
  .brand-name {
    position: absolute;
    display: flex;
    align-items: center;
    gap: 14px;
    font-weight: 400;
    letter-spacing: 0.06em;
    text-transform: uppercase;
    color: var(--ink);
    white-space: nowrap;
  }
  .brand-name__mark {
    width: 16px;
    height: 16px;
    background: var(--ink);
  }
  .card--front .brand-name {
    left: 104px;
    top: 128px;
    font-size: 34px;
  }
  .card--back .brand-name {
    left: 22px;
    top: 38px;
    font-size: 34px;
  }
  .holder {
    position: absolute;
    left: 132px;
    top: 138px;
    color: var(--text);
    font-size: 12.5px;
    line-height: 16px;
  }
  .holder__name {
    font-weight: 700;
    font-size: 14.5px;
    line-height: 18px;
  }
  .holder__title {
    margin-bottom: 17px;
  }
  .holder__address {
    margin-bottom: 5px;
  }
  .card__band {
    position: absolute;
    left: 0;
    bottom: 0;
    width: 545px;
    height: 22px;
  }
</style>
</head>
<body>
  <main class="stage">
    <section class="card card--front" aria-label="Card front">
      <div class="brand-name"><span class="brand-name__mark"></span>Talvik Brensor</div>
    </section>

    <section class="card card--back" aria-label="Card back">
      <div class="brand-name"><span class="brand-name__mark"></span>Talvik Brensor</div>

      <div class="holder">
        <div class="holder__name">Jonas Veberg</div>
        <div class="holder__title">Manger</div>
        <div class="holder__address">Talvik Brensor AS Lindeholtveien<br>7, 3142 Vestskogen 461 82 915</div>
        <div>t: + 999 999 9999</div>
        <div>e: info@brensor.no</div>
        <div>www.brensor.no</div>
      </div>

      <svg class="card__band" viewBox="0 0 545 22" aria-hidden="true">
        <polygon points="0,2 314,2 322,22 0,22" fill="var(--ink)"/>
        <polygon points="322,8 545,8 545,22 328,22" fill="var(--brand-blue)"/>
      </svg>
    </section>
  </main>
</body>
</html>
```